Refresh Brightpath Coursework

Need a new design for e-learning development and web app development site: http://brightpathcoursework.example. Need pages for everything on menu bar plus a training services and a web app development services pages and a better page for samples http://brightpathcoursework.example/samples5/.

***Must be programmed in html 5. NO CMS. No WP. No Plume. Straight html/css.

Target Market(s)

government

Industry/Entity Type

Government

Coding

Coded - Design and coding required

Number of Pages Required

1 page

Requirements
Must have
• Must be coded in html5/css. No CMS.
• Divided so you can easily see that we offer 3 separate services:
• Live Training - E-Learning Development - Web App Development
• A way to display logos of all our clients like on bottom of this page: https://www.quorvatests.example (this is also our website so you can copy all these logos)
• List both our Denver location which is already on our website plus our office in Torvelo Plaza. Street 61 Norte, 17-83. Medellín, Antioquia.
• A page like this for our web app dev services https://www.zemlobuild.example/product-development
Should not have
• CMS

```html
<!DOCTYPE html>
<html lang="en">
<head>
<meta charset="utf-8">
<title>Brightpath Coursework</title>
<link href="https://fonts.googleapis.com/css2?family=Montserrat:wght@600;700&family=Open+Sans:wght@400;600;700&display=swap" rel="stylesheet">
<style>
:root{
  --blue:#1f72b8;
  --blue-mid:#2d86c9;
  --blue-deep:#175f9d;
  --orange:#f7a129;
  --ink:#1b1b1b;
  --text:#4a4a4a;
  --muted:#8a8f96;
  --light:#f3f4f6;
  --white:#ffffff;
}
*{margin:0;padding:0;box-sizing:border-box}
html,body{width:1200px;height:4027px;overflow:hidden}
body{position:relative;background:var(--white);font-family:"Open Sans",Arial,sans-serif;color:var(--text)}
.abs{position:absolute}
h1,h2,h3{font-family:"Montserrat",Arial,sans-serif;font-weight:700}
.accent{color:var(--orange)}

/* header */
.site-header{left:0;top:0;width:1200px;height:102px;background:var(--white)}
.brand{display:flex;align-items:center;gap:12px;left:113px;top:26px}
.brand-dot{width:48px;height:48px;border-radius:50%;background:var(--orange)}
.brand-name{font-family:"Montserrat",sans-serif;font-weight:600;font-size:20px;color:var(--blue);line-height:1.1;width:170px}
.main-nav{right:110px;top:36px;display:flex;gap:40px;font-size:15px;font-weight:600;color:#222}
.main-nav .current{color:var(--blue);border-bottom:3px solid var(--blue);border-radius:0 0 40px 40px;padding:0 6px 6px}

/* hero */
.hero{left:0;top:102px;width:1200px;height:703px;background:linear-gradient(180deg,#2a7cc0,#1c68ab)}
.hero-art{left:200px;top:0;width:800px;height:650px;background:radial-gradient(ellipse at center,rgba(255,255,255,.14),rgba(255,255,255,0) 70%)}
.hero-curve{left:0;top:640px}
.hero-title{left:0;top:232px;width:1200px;text-align:center;font-size:62px;line-height:80px;letter-spacing:3px;color:var(--white);font-weight:600;white-space:nowrap}
.hero-sub{left:0;top:320px;width:1200px;text-align:center;font-size:25px;line-height:34px;color:var(--white);white-space:nowrap}
.btn{display:block;text-align:center;font-weight:700;color:var(--white);border-radius:30px;font-size:16px}
.btn-start{left:503px;top:386px;width:194px;height:60px;line-height:60px;background:var(--orange)}

/* welcome */
.welcome-mark{left:570px;top:866px;width:60px;height:60px;border-radius:50%;background:var(--orange)}
.welcome-title{left:0;top:937px;width:1200px;text-align:center;font-size:38px;color:var(--ink)}
.welcome-copy{left:148px;top:1004px;width:904px;text-align:center;font-size:16px;line-height:32px}
.welcome-copy p+p{margin-top:32px}
.btn-more{left:461px;top:1278px;width:278px;height:60px;line-height:60px;background:var(--blue-deep);font-size:15px}

/* services */
.service{left:0;width:1200px}
.service-light{background:var(--light)}
.service-blue{background:linear-gradient(180deg,var(--blue-mid),#2173b5)}
.service-circle{width:332px;height:332px;border-radius:50%;background:var(--white);box-shadow:0 10px 0 var(--blue-deep),0 12px 30px rgba(0,0,0,.12);display:flex;align-items:center;justify-content:center}
.service-icon{width:140px;height:120px;border-radius:10px;background:linear-gradient(135deg,var(--orange),#f08a16 60%,var(--blue-deep))}
.service-title{font-size:38px;color:var(--ink)}
.service-blue .service-title{color:var(--white)}
.service-copy{font-size:16px;line-height:32px;color:#444}
.service-blue .service-copy{color:#e4eef7}

/* clients */
.clients-title{left:0;top:3058px;width:1200px;text-align:center;font-size:38px;color:var(--ink)}
.client-row{left:100px;width:1000px;display:flex;justify-content:space-between;align-items:center;height:90px}
.client-name{font-family:"Montserrat",sans-serif;font-weight:600;font-size:22px;color:#2c4f7c}
.client-seal{width:72px;height:72px;border-radius:50%;background:#c9ccd1}
.client-shield{width:66px;height:78px;border-radius:8px;background:#c9ccd1}

/* footer */
.site-footer{left:0;top:3598px;width:1200px;height:429px;background:linear-gradient(180deg,var(--blue),#1b66a8);color:var(--white)}
.footer-brand{left:113px;top:122px;display:flex;align-items:center;gap:12px}
.footer-brand .brand-dot{background:var(--white)}
.footer-brand .brand-name{color:var(--white)}
.footer-head{font-family:"Montserrat",sans-serif;font-size:22px;font-weight:700}
.footer-line{display:flex;gap:10px;font-size:15px;line-height:26px;white-space:nowrap}
.footer-line.wrap{white-space:normal}
.footer-line svg{flex:none;margin-top:6px}
.social{display:flex;gap:12px}
.social span{width:44px;height:44px;border-radius:50%;background:var(--white)}
.copyright{left:0;top:374px;width:1200px;text-align:center;font-size:15px;color:#dfe9f3}
</style>
</head>
<body>

<header class="site-header abs">
  <div class="brand abs"><span class="brand-dot"></span><span class="brand-name">Brightpath Coursework</span></div>
  <nav class="main-nav abs">
    <span class="current">HOME</span><span>ABOUT US</span><span>OUR SERVICES</span><span>PARTNERS</span><span>CONTACT US</span>
  </nav>
</header>

<section class="hero abs">
  <div class="hero-art abs" role="img" aria-label="Illustration of people learning around a large laptop"></div>
  <svg class="hero-curve abs" width="1200" height="70" viewBox="0 0 1200 70" aria-hidden="true">
    <path d="M0 0 Q600 140 1200 0 L1200 70 L0 70 Z" fill="#ffffff"/>
  </svg>
  <h1 class="hero-title abs">BRIGHTPATH COURSEWORK</h1>
  <p class="hero-sub abs">We are a e-learning development and web app development</p>
  <a class="btn btn-start abs">GET STARTED</a>
</section>

<section>
  <div class="welcome-mark abs"></div>
  <h2 class="welcome-title abs">Welcome to <span class="accent">Brightpath Coursework</span></h2>
  <div class="welcome-copy abs">
    <p>Lorem ipsum dolor sit amet, consectetur adipiscing elit, sed do eiusmod tempor incididunt ut labore et dolore magna aliqua. Ut enim ad minim veniam, quis nostrud exercitation ullamco laboris nisi ut aliquip ex ea commodo consequat. Duis aute irure dolor in reprehenderit in voluptate velit esse cillum dolore eu fugiat nulla pariatur. Excepteur sint occaecat cupidatat non proident, sunt in culpa qui officia deserunt mollit anim id est laborum.</p>
    <p>Sed ut perspiciatis unde omnis iste natus error sit voluptatem accusantium doloremque laudantium, totam rem aperiam, eaque ipsa quae ab illo inventore veritatis et quasi architecto beatae vitae dicta sunt explicabo</p>
  </div>
  <a class="btn btn-more abs">READ MORE INFORMATION</a>
</section>

<section class="service service-light abs" style="top:1439px;height:494px">
  <div class="service-circle abs" style="left:111px;top:68px"><div class="service-icon" role="img" aria-label="Icon of a trainer presenting to a group"></div></div>
  <h3 class="service-title abs" style="left:521px;top:120px">Live <span class="accent">Training Services</span></h3>
  <p class="service-copy abs" style="left:521px;top:188px;width:540px">Lorem ipsum dolor sit amet, consectetur adipiscing elit, sed do eiusmod tempor incididunt ut labore et dolore magna aliqua. Ut enim ad minim veniam, quis nostrud exercitation ullamco laboris nisi ut aliquip ex ea commodo consequat. Duis aute irure dolor in reprehenderit in voluptate velit esse cillum dolore eu fugiat nulla pariatur.</p>
</section>

<section class="service service-blue abs" style="top:1933px;height:516px">
  <h3 class="service-title abs" style="left:110px;top:140px">E-Learning <span class="accent">Development</span></h3>
  <p class="service-copy abs" style="left:110px;top:208px;width:580px">Sed ut perspiciatis unde omnis iste natus error sit voluptatem accusantium doloremque laudantium, totam rem aperiam, eaque ipsa quae ab illo inventore veritatis et quasi architecto beatae vitae dicta sunt explicabo. Nemo enim ipsam voluptatem quia voluptas sit aspernatur aut odit aut fugit, sed quia consequuntur magni dolores eos qui ratione voluptatem sequi nesciunt.</p>
  <div class="service-circle abs" style="left:755px;top:84px"><div class="service-icon" role="img" aria-label="Icon of a person working at a desk"></div></div>
</section>

<section class="service service-light abs" style="top:2449px;height:523px">
  <div class="service-circle abs" style="left:111px;top:97px"><div class="service-icon" role="img" aria-label="Icon of desktop, tablet and phone screens"></div></div>
  <h3 class="service-title abs" style="left:521px;top:146px">Web <span class="accent">App Development</span></h3>
  <p class="service-copy abs" style="left:521px;top:214px;width:540px">At vero eos et accusamus et iusto odio dignissimos ducimus qui blanditiis praesentium voluptatum deleniti atque corrupti quos dolores et quas molestias excepturi sint occaecati cupiditate non provident, similique sunt in culpa qui officia deserunt mollitia animi, id est laborum et dolorum fuga. Et harum quidem rerum facilis est et expedita distinctio.</p>
</section>

<section>
  <h2 class="clients-title abs">Our <span class="accent">Clients Partner</span></h2>
  <div class="client-row abs" style="top:3155px">
    <span class="client-name">Aerovant</span><span class="client-seal"></span><span class="client-seal"></span><span class="client-shield"></span><span class="client-seal"></span><span class="client-name">Stelvane</span><span class="client-name">Sunharrow</span><span class="client-name">Redmarch</span>
  </div>
  <div class="client-row abs" style="top:3284px;left:150px;width:900px">
    <span class="client-seal"></span><span class="client-name">Stanholt</span><span class="client-name">Vernmoor College</span><span class="client-name">Biolattice</span><span class="client-seal"></span><span class="client-seal"></span>
  </div>
  <div class="client-row abs" style="top:3413px">
    <span class="client-seal"></span><span class="client-name">Ridgefield State</span><span class="client-name">Westvale</span><span class="client-seal"></span><span class="client-shield"></span><span class="client-seal"></span><span class="client-name">Akrelo</span>
  </div>
</section>

<footer class="site-footer abs">
  <div class="footer-brand abs"><span class="brand-dot"></span><span class="brand-name">Brightpath Coursework</span></div>

  <div class="abs" style="left:459px;top:92px;width:370px">
    <h4 class="footer-head">LOCATION</h4>
    <div class="footer-line wrap" style="margin-top:18px;width:300px">
      <svg width="12" height="16" viewBox="0 0 12 16"><path d="M6 0a6 6 0 0 0-6 6c0 4.5 6 10 6 10s6-5.5 6-10a6 6 0 0 0-6-6zm0 8.5A2.5 2.5 0 1 1 6 3.5a2.5 2.5 0 0 1 0 5z" fill="#fff"/></svg>
      <span>5820 Larkspur Avenue, Suite 2-118, Halden, CO. 80990</span>
    </div>
    <div class="footer-line" style="margin-top:20px">
      <svg width="14" height="14" viewBox="0 0 14 14"><path d="M3 0l2.5 3.5-1.5 1.5a8 8 0 0 0 5 5l1.5-1.5L14 11l-2 3C5 13 1 9 0 2z" fill="#fff"/></svg>
      <span>Telephone: +1 555 014 7390</span>
    </div>
    <div class="footer-line" style="margin-top:24px">
      <svg width="16" height="12" viewBox="0 0 16 12"><rect width="16" height="12" rx="1.5" fill="#fff"/><path d="M1 1.5l7 5 7-5" stroke="#1f72b8" stroke-width="1.5" fill="none"/></svg>
      <span>Email:support@brightpathcoursework.example</span>
    </div>
  </div>

  <div class="abs" style="left:843px;top:92px;width:260px">
    <h4 class="footer-head">OUR OFFICE</h4>
    <p style="font-size:15px;line-height:26px;margin-top:14px">Torvelo Plaza. Street 61 Norte, 17-83.<br>Medellín, Antioquia.</p>
    <h4 class="footer-head" style="margin-top:14px">GET IN TOUCH</h4>
    <div class="social" style="margin-top:14px" aria-label="Social links"><span></span><span></span><span></span></div>
  </div>

  <p class="copyright abs">Copyrights © 2019 Brightpath Coursework Solutions. All rights reserved.</p>
</footer>

</body>
</html>
```